チラシに使用する文章と画像はこちらで用意いたします。
全体の雰囲気はimageBのような感じです。
作りたいチラシのイメージはimageAのとおりです。
デザインは自由に調整いただいてかまいません。
使用する色はimageBのような「黒、茶」を考えておりますが、自由に調整いただいて結構です。

使用する文章はPDFファイルを参照下さい。
imageAのAからIはPDFの文章を入れて下さい。

imageAのDにいれる画像は「health.zip」をご使用下さい。
imageAのEにいれる画像は「urinary organs.zip」をご使用下さい。
imageAのFにいれる画像は「digestive organs.zip」をご使用下さい。
画像はimageBのように並べて下さい。

またimageAのD、E、Fのハーブの画像の上に「ORU・PLANTIVA」のマークを入れて下さい。
詳しくはimageAをご参照ください。
マークの画像はimageCをお使い下さい。
有機農作物はマークがないため、有機農作物と記載して下さい。
A4
片面
黒 茶色
• 高解像度JPG (.jpg)
• イラストレーター形式 (.ai)

柔らかい雰囲気やデザインなどとても気に入りました。
色合いも落ち着いているので、読みやすかったです。

たくさん提案くださり、誠にありがとうございます。
また機会があれば、どうぞよろしくお願い致します。

```html
<!DOCTYPE html>
<html lang="ja">
<head>
<meta charset="utf-8">
<title>ハーブ チラシ</title>
<link href="https://fonts.googleapis.com/css2?family=M+PLUS+Rounded+1c:wght@500;700;800&family=Noto+Sans+JP:wght@400;500;700&display=swap" rel="stylesheet">
<style>
:root{
  --green:#7bb84a;
  --green-soft:#a9d08a;
  --green-pale:#e4f0d6;
  --brown:#7a4a22;
  --ink:#3b3128;
  --muted:#6b5f55;
  --paper:#fbfaf6;
  --line:#c9b9a5;
}
*{box-sizing:border-box;margin:0;padding:0}
html,body{width:851px;height:1200px;overflow:hidden;background:var(--paper)}
body{position:relative;font-family:"Noto Sans JP",sans-serif;color:var(--ink)}
.headline{position:absolute;left:34px;top:26px;font-family:"M PLUS Rounded 1c",sans-serif;font-weight:800;color:var(--green);font-size:46px;line-height:1.3;letter-spacing:1px}
.dog-art{position:absolute;left:470px;top:0;width:340px;height:320px;border-radius:40% 45% 30% 40%;background:radial-gradient(circle at 60% 40%,var(--green-soft),var(--green-pale) 75%,transparent 76%)}
.cat-art{position:absolute;left:160px;top:200px;width:160px;height:370px;border-radius:45% 45% 30% 30%;background:linear-gradient(180deg,var(--green-pale),var(--green-soft))}
.intro{position:absolute;left:440px;top:176px;width:370px;font-size:10.5px;line-height:1.7;color:var(--muted)}
.intro h2{font-size:15px;color:var(--brown);font-weight:700;margin-bottom:6px}
.intro h3{font-size:14px;color:var(--brown);font-weight:700;margin:12px 0 4px}
.product{position:absolute;left:34px;width:790px;height:130px}
.product .label{display:inline-block;background:var(--green);color:#fff;font-weight:700;font-size:13px;padding:3px 8px;border-radius:3px}
.product .price{font-size:15px;font-weight:700;color:var(--brown);margin:4px 0 3px}
.product .price small{font-size:12px}
.product .desc{width:220px;font-size:9px;line-height:1.55;color:var(--muted)}
.herbs{position:absolute;left:260px;top:0;display:flex;gap:12px}
.herb{width:96px;text-align:center}
.herb .tag{display:inline-block;font-size:8px;border:1px solid var(--brown);color:var(--brown);padding:0 4px;margin-bottom:3px}
.herb .photo{width:96px;height:82px;border-radius:4px}
.herb .name{font-size:9px;margin-top:3px;color:var(--ink)}
.g1{background:linear-gradient(135deg,#8a6a43,#b8956a)}
.g2{background:linear-gradient(135deg,#7f9a4e,#b5c98a)}
.g3{background:linear-gradient(135deg,#6e5233,#a88256)}
.g4{background:linear-gradient(135deg,#6f8e45,#9fbb72)}
.g5{background:linear-gradient(135deg,#d9cdb6,#f1ead9)}
.g6{background:linear-gradient(135deg,#b4a16a,#e0cf8f)}
.g7{background:linear-gradient(135deg,#b0483a,#d9836b)}
.g8{background:linear-gradient(135deg,#c9b86a,#efe3a9)}
.g9{background:linear-gradient(135deg,#5d8a3f,#93bd6e)}
.rule{position:absolute;left:34px;width:783px;border-top:1px dashed var(--line)}
.legend{position:absolute;left:34px;top:1010px;width:783px;display:flex;gap:24px}
.legend .col{flex:1;font-size:9px;line-height:1.6;color:var(--muted)}
.legend .mark{display:flex;align-items:center;gap:6px;font-size:11px;font-weight:700;color:var(--brown);margin-bottom:6px}
.legend .dot{width:18px;height:18px;border-radius:50%;border:2px solid var(--green)}
.legend .box{border:1.5px solid var(--brown);padding:1px 8px;font-size:11px}
</style>
</head>
<body>
<div class="dog-art" role="img" aria-label="犬のシルエットイラスト"></div>
<div class="cat-art" role="img" aria-label="猫のシルエットイラスト"></div>

<h1 class="headline">大切な家族だから<br>いつまでも若々しく<br>元気にいてほしい。</h1>

<section class="intro">
  <h2>現代の犬、猫にこそハーブをおすすめします</h2>
  <p>食生活や環境の変化により、犬や猫の体にも負担がかかりやすくなっています。毎日のごはんに少量のハーブを加えることで、自然の力をやさしく取り入れ、健やかな毎日をサポートします。</p>
  <h3>特筆すべきは抗酸化作用</h3>
  <p>ハーブには抗酸化成分が豊富に含まれ、年齢とともに気になる変化に寄り添います。いつまでも若々しく過ごすための心強い味方です。</p>
  <h3>腸内環境を整える</h3>
  <p>食物繊維を含むハーブは腸内環境を整え、毎日のすっきりを助けます。体の内側から元気をつくりましょう。</p>
</section>

<section class="product" style="top:585px">
  <span class="label">健康維持応援ハーブ</span>
  <p class="price">25g入り <small>1,260円</small></p>
  <p class="desc">毎日の健康維持に役立つハーブをバランスよくブレンド。いつものごはんにひとさじ加えるだけで手軽に続けられます。</p>
  <div class="herbs">
    <div class="herb"><span class="tag">有機農産物</span><div class="photo g1" role="img" aria-label="バードックルートの写真"></div><p class="name">バードックルート</p></div>
    <div class="herb"><span class="tag">有機農産物</span><div class="photo g2" role="img" aria-label="ダンデライオンリーフの写真"></div><p class="name">ダンデライオンリーフ</p></div>
    <div class="herb"><span class="tag">有機農産物</span><div class="photo g3" role="img" aria-label="ダンデライオンルートの写真"></div><p class="name">ダンデライオンルート</p></div>
    <div class="herb"><span class="tag">有機農産物</span><div class="photo g4" role="img" aria-label="ネトルの写真"></div><p class="name">ネトル</p></div>
    <div class="herb"><span class="tag">有機農産物</span><div class="photo g5" role="img" aria-label="マシュマロウの写真"></div><p class="name">マシュマロウ</p></div>
  </div>
</section>
<div class="rule" style="top:720px"></div>

<section class="product" style="top:735px">
  <span class="label">泌尿器系応援ハーブ</span>
  <p class="price">25g入り <small>1,260円</small></p>
  <p class="desc">尿路の健康を気づかうハーブを組み合わせました。水分補給とあわせて、毎日のすこやかな巡りをサポートします。</p>
  <div class="herbs">
    <div class="herb"><span class="tag">有機農産物</span><div class="photo g2" role="img" aria-label="ダンデライオンリーフの写真"></div><p class="name">ダンデライオンリーフ</p></div>
    <div class="herb"><span class="tag">有機農産物</span><div class="photo g5" role="img" aria-label="マシュマロウの写真"></div><p class="name">マシュマロウ</p></div>
    <div class="herb"><span class="tag">有機農産物</span><div class="photo g4" role="img" aria-label="ネトルの写真"></div><p class="name">ネトル</p></div>
    <div class="herb"><span class="tag">有機農産物</span><div class="photo g6" role="img" aria-label="コーンシルクの写真"></div><p class="name">コーンシルク</p></div>
    <div class="herb"><span class="tag">有機農産物</span><div class="photo g7" role="img" aria-label="ローズヒップの写真"></div><p class="name">ローズヒップ</p></div>
  </div>
</section>
<div class="rule" style="top:870px"></div>

<section class="product" style="top:885px">
  <span class="label">消化器系応援ハーブ</span>
  <p class="price">25g入り <small>1,260円</small></p>
  <p class="desc">おなかの調子を整えるハーブをブレンド。食欲や消化が気になる子の毎日のごはんにおすすめです。</p>
  <div class="herbs">
    <div class="herb"><span class="tag">有機農産物</span><div class="photo g2" role="img" aria-label="ダンデライオンリーフの写真"></div><p class="name">ダンデライオンリーフ</p></div>
    <div class="herb"><span class="tag">有機農産物</span><div class="photo g8" role="img" aria-label="カモミールの写真"></div><p class="name">カモミール</p></div>
    <div class="herb"><span class="tag">有機農産物</span><div class="photo g4" role="img" aria-label="ネトルの写真"></div><p class="name">ネトル</p></div>
    <div class="herb"><span class="tag">有機農産物</span><div class="photo g5" role="img" aria-label="マシュマロウの写真"></div><p class="name">マシュマロウ</p></div>
    <div class="herb"><span class="tag">有機農産物</span><div class="photo g9" role="img" aria-label="ペパーミントの写真"></div><p class="name">ペパーミント</p></div>
  </div>
</section>

<section class="legend">
  <div class="col"><p class="mark"><span class="dot"></span>認証ハーブ</p><p>認証機関の基準を満たした方法で栽培・加工されたハーブです。安心してお使いいただけます。</p></div>
  <div class="col"><p class="mark"><span class="dot"></span>ORU・PLANTIVA</p><p>ORU・PLANTIVAの認証を受けたハーブです。厳しい基準のもとで管理されています。</p></div>
  <div class="col"><p class="mark"><span class="box">有機農産物</span></p><p>化学肥料や農薬に頼らず育てられた有機農産物です。素材本来の力をそのまま届けます。</p></div>
</section>
</body>
</html>
```